Brevlo core services brochure

I need a brochure to give to people who haven’t used our services which are:

Managed Infrastructure & Risk Assessment
Digital Business & Cloud Solutions
Backup, Disaster Recovery & Unified Business Continuity

Our services overview is here: https://www.brevlo-example.com.au/wp-content/uploads/Brevlo-Core-Services-Overview.pdf

It needs a short summarised version with some new graphics that use the same colours as the logo and possibly some transitions or swirls that use similar design characteristics.

```html
<!DOCTYPE html>
<html lang="en">
<head>
<meta charset="utf-8">
<title>Brevlo – Our Services</title>
<link rel="stylesheet" href="https://fonts.googleapis.com/css2?family=Cabin:wght@400;600&family=Arimo:wght@400&display=swap">
<style>
  :root {
    --brand-blue: #3a67b1;
    --band-grey: #454545;
    --ink: #1d1d1d;
    --rule: #4a4a4a;
    --paper: #ffffff;
  }
  * { margin: 0; padding: 0; box-sizing: border-box; }
  html, body { width: 848px; height: 1200px; overflow: hidden; background: var(--paper); }
  .page { position: relative; width: 848px; height: 1200px; overflow: hidden; font-family: "Cabin", "Gill Sans", sans-serif; color: var(--ink); }

  .title-tab { position: absolute; left: 0; top: 76px; width: 82px; height: 39px; background: var(--brand-blue); }
  .title-square { position: absolute; left: 310px; top: 76px; width: 36px; height: 39px; background: var(--band-grey); }
  .page-title { position: absolute; left: 89px; top: 78px; font-family: "Cabin", sans-serif; font-weight: 600; font-size: 29px; color: var(--brand-blue); letter-spacing: 0.3px; }

  .service-band { position: absolute; left: 0; top: 174px; width: 848px; height: 226px; background: var(--band-grey); }
  .service { position: absolute; top: 44px; width: 260px; text-align: center; color: #fff; }
  .service svg { display: block; margin: 0 auto; width: 82px; height: 78px; }
  .service-name { margin-top: 12px; font-size: 22px; line-height: 25px; font-weight: 400; }
  .service--infra { left: 70px; }
  .service--cloud { left: 324px; }
  .service--continuity { left: 551px; }

  .product-visual { position: absolute; left: 24px; top: 432px; width: 800px; height: 320px;
    background: radial-gradient(ellipse at 62% 45%, #e9eef4 0%, #d9dfe6 35%, #ffffff 72%); }

  .intro { position: absolute; left: 73px; top: 802px; width: 700px; }
  .intro h2 { font-family: "Arimo", Arial, sans-serif; font-weight: 400; font-size: 36px; color: var(--brand-blue); line-height: 40px; }
  .intro p { margin: 2px 0 0 5px; font-size: 15.5px; line-height: 19.5px; width: 660px; }

  .divider { position: absolute; left: 72px; top: 931px; width: 704px; height: 1px; background: var(--rule); }
  .column-split { position: absolute; left: 414px; top: 931px; width: 1px; height: 194px; background: var(--rule); }

  .feature { position: absolute; top: 944px; width: 320px; }
  .feature h3 { font-family: "Arimo", Arial, sans-serif; font-weight: 400; font-size: 35px; line-height: 36px; color: var(--brand-blue); }
  .feature p { margin-top: 8px; font-size: 15.5px; line-height: 19.2px; }
  .feature--infra { left: 72px; }
  .feature--scale { left: 448px; }
</style>
</head>
<body>
<main class="page">
  <div class="title-tab"></div>
  <h1 class="page-title">Our Services</h1>
  <div class="title-square"></div>

  <section class="service-band">
    <div class="service service--infra">
      <svg viewBox="0 0 82 78" fill="none" stroke="#fff" stroke-width="2.6" stroke-linecap="round" stroke-linejoin="round">
        <ellipse cx="26" cy="9" rx="23" ry="7"/>
        <path d="M3 9v44c0 4 10 7 23 7"/>
        <path d="M49 9v14"/>
        <path d="M3 23c0 4 10 7 23 7 6 0 11-1 15-2"/>
        <path d="M3 38c0 4 10 7 23 7"/>
        <circle cx="67" cy="26" r="6"/>
        <path d="M67 14v4M67 34v4M55 26h4M75 26h4M59 18l3 3M72 31l3 3M59 34l3-3M72 21l3-3"/>
        <circle cx="48" cy="57" r="7"/>
        <path d="M48 42v5M48 67v5M33 57h5M58 57h5M37 46l4 4M55 64l4 4M37 68l4-4M55 50l4-4"/>
      </svg>
      <div class="service-name">Managed Infrastructure<br>&amp; Risk Assessment</div>
    </div>
    <div class="service service--cloud">
      <svg viewBox="0 0 124 78" style="width:124px" fill="none" stroke="#fff" stroke-width="2.6" stroke-linecap="round" stroke-linejoin="round">
        <rect x="2" y="16" width="56" height="40" rx="2"/>
        <path d="M2 23h56M6 19.5h2M11 19.5h2M16 19.5h2"/>
        <path d="M10 50v-6M16 50v-10M22 50v-14M28 50v-18M8 51h24"/>
        <path d="M22 56v8M14 66h18"/>
        <path d="M36 32h10l4-4h6M36 38h14l4 4M36 44h8"/>
        <circle cx="86" cy="30" r="11"/>
        <path d="M82 41v6h8v-6M83 50h6M86 8v-6M70 14l-4-4M102 14l4-4M66 30h-6M106 30h6"/>
        <path d="M60 66c-6 0-9-5-7-10 2-4 6-5 9-4 2-6 10-8 14-4M96 44c4-2 12 0 13 7 6 0 9 5 7 10-1 3-4 5-7 5H60"/>
        <circle cx="104" cy="60" r="6"/>
        <path d="M101 60l2 2 4-4M66 60h12M66 66h12"/>
      </svg>
      <div class="service-name">Digital Business<br>&amp; Cloud Solutions</div>
    </div>
    <div class="service service--continuity">
      <svg viewBox="0 0 78 78" fill="none" stroke="#fff" stroke-width="2.6" stroke-linecap="round" stroke-linejoin="round">
        <path d="M12 22A32 32 0 0 1 62 12M66 16l-3-5-5 1"/>
        <path d="M71 36a32 32 0 0 1-16 31"/>
        <path d="M45 70A32 32 0 0 1 7 44M5 49l2-5 5 1"/>
        <path d="M6 36A32 32 0 0 1 9 26"/>
        <path d="M39 21l4 1 2 5 5-1 3 4-3 4 2 5-3 3-4 1-2 5h-5l-1-5-5-1-3 3-4-3 2-5-3-3 1-4 5-1 2-5z"/>
        <circle cx="39" cy="37" r="8"/>
      </svg>
      <div class="service-name">Unified Business<br>Continuity</div>
    </div>
  </section>

  <div class="product-visual" role="img" aria-label="Product photo: two tablet computers with business dashboards on screen, a blue keyboard cover and a stylus"></div>

  <section class="intro">
    <h2>Your Business Specialist</h2>
    <p>Brevlo provides a variety of business support services to facilitate your IT requirements. Our dedicated team of professionals will help you source, customise and install the right technology for your business.</p>
  </section>

  <div class="divider"></div>
  <div class="column-split"></div>

  <section class="feature feature--infra">
    <h3>Infrastructure<br>Services</h3>
    <p>Our managed infrastructure services are tailored for on-going infrastructure support within business environments that demand comprehensive pro-active monitoring, support and maintenance.</p>
  </section>

  <section class="feature feature--scale">
    <h3>Business Support<br>Scalability</h3>
    <p>We cater to business infrastructure of all shapes and sizes and always maintain a high level of care. For peace of mind, upon entering a service agreement we provide a free on-site audit of your infrastructure.</p>
  </section>
</main>
</body>
</html>
```